Menu Design Project

This is a sushi menu. We need to polish the menu. You can re-size logo and add color and graphic to make inviting. Please feel free to make any recommendations.

Target Market(s)

Upscale crowd

```html
<!DOCTYPE html>
<html lang="en">
<head>
<meta charset="utf-8">
<title>Kaiyo Sushi Bar — Menu</title>
<link href="https://fonts.googleapis.com/css2?family=Archivo:wght@800&family=Arimo:ital,wght@0,400;0,700;1,400&family=Oswald:wght@600&display=swap" rel="stylesheet">
<style>
  :root {
    --paper-light: #f3e9d6;
    --paper: #ecdfc6;
    --paper-dark: #e2d2b4;
    --ink: #141210;
    --brand-red: #d3302a;
  }
  * { margin: 0; padding: 0; box-sizing: border-box; }
  html, body { width: 800px; height: 1200px; overflow: hidden; }
  body {
    position: relative;
    background: radial-gradient(ellipse at 50% 40%, var(--paper-light) 0%, var(--paper) 60%, var(--paper-dark) 100%);
    color: var(--ink);
    font-family: "Arimo", Arial, sans-serif;
  }
  .brand { position: absolute; top: 22px; left: 0; width: 800px; text-align: center; }
  .brand-mark { display: block; margin: 0 auto; }
  .brand-name {
    font-family: "Oswald", "Arial Narrow", sans-serif;
    font-weight: 600;
    color: var(--ink);
    line-height: 1;
    text-shadow: none;
  }
  .brand-name .primary { display: block; font-size: 50px; letter-spacing: 2px; margin-top: 22px; }
  .brand-name .secondary { display: block; font-size: 21px; letter-spacing: 5px; margin-top: 6px; }

  .column { position: absolute; }
  .col-left { left: 42px; width: 225px; }
  .col-mid { left: 305px; width: 225px; }
  .col-right { left: 570px; width: 205px; }

  .section { position: absolute; left: 0; width: 100%; }
  .section-title {
    font-family: "Archivo", "Arial Black", sans-serif;
    font-weight: 800;
    font-size: 38px;
    line-height: 40px;
    letter-spacing: -0.3px;
    margin-bottom: 14px;
    text-shadow: none;
  }
  .section-note { font-size: 7.6px; font-style: italic; margin: -10px 0 12px; }
  .item { font-size: 7.4px; line-height: 9.4px; margin-bottom: 7.2px; }
  .item b { font-weight: 700; }
  .item.tight { margin-bottom: 3px; }
  .variants { font-weight: 700; }
  .price { font-weight: 700; }
  .group { font-size: 7.4px; line-height: 9.4px; margin-bottom: 9px; }

  .footer {
    position: absolute; left: 0; top: 1162px; width: 800px;
    text-align: center; font-size: 7.4px; line-height: 9.6px; font-style: italic;
  }
</style>
</head>
<body>

<header class="brand">
  <svg class="brand-mark" width="150" height="150" viewBox="0 0 150 150" aria-hidden="true">
    <circle cx="75" cy="75" r="72" fill="var(--brand-red)"/>
  </svg>
  <h1 class="brand-name"><span class="primary">KAIYO</span><span class="secondary">SUSHI BAR</span></h1>
</header>

<div class="column col-left">
  <section class="section" style="top:312px">
    <h2 class="section-title">appetizers</h2>
    <p class="item"><b>edamame</b> soybeans &amp; seasalt <span class="price">3.5</span></p>
    <p class="item"><b>spicy garlic edamame</b> soybeans, seasalt &amp; spicy garlic <span class="price">4.5</span></p>
    <p class="item"><b>sautéed asparagus</b> asparagus &amp; teriyaki sauce <span class="price">4.5</span></p>
    <p class="item"><b>sautéed shiitake</b> mushrooms, onions &amp; cream sauce <span class="price">5</span></p>
    <p class="item"><b>age dashi tofu</b> tofu, sweet dashi soy sauce &amp; bonito flakes <span class="price">5</span></p>
    <p class="item"><b>yakitori teriyaki</b> chicken &amp; vegetables served on skewers <span class="price">6</span></p>
    <p class="item"><b>gyoza</b> beef &amp; vegetable dumplings <span class="price">5.5</span></p>
    <p class="item"><b>shumai</b> shrimp dumplings &amp; ponzu sauce <span class="price">5.5</span></p>
    <p class="item"><b>soft-shell crab</b> fried soft-shell crab &amp; ponzu sauce <span class="price">9</span></p>
    <p class="item"><b>tatsuta-age</b> panko breaded chicken, garlic<br>&amp; tempura sauce <span class="price">6</span></p>
    <p class="item"><b>tako su</b> octopus marinated in citrus sauce <span class="price">7</span></p>
    <p class="item"><b>calamari rings</b> fried calamari &amp; tempura sauce <span class="price">8</span></p>
    <p class="item"><b>grilled calamari</b> grilled calamari marinated in lemon teriyaki sauce, garlic &amp; ginger <span class="price">8</span></p>
    <p class="item"><b>hamachi kama</b> yellowtail collar &amp; ponzu sauce <span class="price">8</span></p>
    <p class="item"><b>mixed tempura</b> tempura shrimp &amp; vegetables <span class="price">7</span></p>
    <p class="item"><b>vegetable tempura</b> tempura vegetables <span class="price">6</span></p>
    <p class="item"><b>chicken katsu</b> breaded chicken skewers &amp; japanese barbecue sauce <span class="price">5.5</span></p>
  </section>

  <section class="section" style="top:695px">
    <h2 class="section-title">soup</h2>
    <p class="item"><b>miso soup</b> tofu, scallions, seaweed &amp; miso broth <span class="price">2</span></p>
    <p class="item"><b>mushroom miso soup</b> tofu, scallions, enoki &amp; shiitake <span class="price">4</span></p>
    <p class="item"><b>suimono</b> japanese clear soup <span class="price">2</span></p>
    <p class="item"><b>ishikari nabe</b> salmon, miso broth &amp; vegetables <span class="price">8</span></p>
  </section>

  <section class="section" style="top:832px">
    <h2 class="section-title">salads</h2>
    <p class="item"><b>house salad</b> mixed greens, vegetables &amp; ginger dressing <span class="price">2.5</span></p>
    <p class="item"><b>tofu salad</b> house salad, tofu, bonito flakes<br>&amp; sesame dressing <span class="price">4</span></p>
    <p class="item"><b>seaweed salad</b> marinated seaweed, sesame seeds<br>&amp; sesame oil <span class="price">4</span></p>
    <p class="item"><b>avocado salad</b> house salad &amp; avocado <span class="price">4</span></p>
    <p class="item"><b>spicy tuna salad*</b> spicy tuna, cucumber, masago, daikon,<br>spring mix &amp; citrus sauce <span class="price">10</span></p>
    <p class="item"><b>crab salad</b> crab salad, cucumber, daikon, spring mix &amp;<br>sesame dressing <span class="price">8</span></p>
    <p class="item"><b>spicy seafood salad*</b> shrimp, spicy scallop, crabstick,<br>cucmber, daikon, spring mix &amp; sesame dressing <span class="price">10</span></p>
    <p class="item"><b>ika salad</b> squid salad &amp; japanese mountain vegetables <span class="price">6.5</span></p>
  </section>
</div>

<div class="column col-mid">
  <section class="section" style="top:312px">
    <h2 class="section-title">noodles</h2>
    <p class="item"><b>mori soba</b> chilled buckwheat noodles &amp; dipping sauce <span class="price">7</span></p>
    <p class="item"><b>tempura udon</b> japanese udon noodles, shrimp, seafood<br>&amp; vegetable tempura <span class="price">10</span></p>
    <p class="item"><b>kake udon</b> japanese udon noodles, clear broth, scallions,<br>seaweed, fried tofu &amp; fish cake <span class="price">7</span></p>
    <p class="item"><b>yaki udon</b> stir-fried chicken, cabbage, onions, scallions,<br>carrots, bean sprouts &amp; seaweed flakes <span class="price">10</span></p>
    <p class="item"><b>vegetable udon</b> japanese udon noodles, vegetables, tofu &amp;<br>clear broth <span class="price">8</span></p>
    <p class="item tight"><b>nabeyaki</b> udon japanese udon noodles, egg &amp;<br>shrimp tempura <span class="price">11</span><br><b>add seafood</b> (mussle, shrimp, scallop &amp; calamari) <span class="price">13</span></p>
    <p class="item" style="margin-top:7px"><b>spicy seafood</b> udon sautéed shrimp, scallop, calamari,<br>mussle, asparagus, zucchini &amp; carrots <span class="price">15</span></p>
    <p class="item"><b>yakisoba</b> stir-fried soba noodles &amp; vegetables<br><span class="variants">beef 11</span></p>
    <p class="item"><b>seafood</b> (shrimp, scallop &amp; calamari) <span class="price">14</span></p>
    <p class="item"><b>seafood noodle soup</b> noodle soup, vegetables, mussle,<br>shrimp, scallop &amp; calamari <span class="price">11</span></p>
  </section>

  <section class="section" style="top:645px">
    <h2 class="section-title">entrées</h2>
    <div class="group"><b>teriyaki</b> teriyaki sauce, sesame seeds &amp; vegetables served with a side of miso soup, house salad &amp; rice
      <div class="variants">salmon 15<br>chicken 12<br>beef 15<br>beef &amp; chicken 16<br>salmon w/ shrimp &amp; vegetable tempura 17<br>chicken w/ shrimp &amp; vegetable tempura 16<br>beef w/ shrimp &amp; vegetable tempura 17</div></div>
    <div class="group"><b>katsu</b> breaded cutlet, japanese barbecue sauce &amp; shredded cabbage served with miso soup, house salad &amp; rice
      <div class="variants">chicken 12<br>beef 15<br>tonkatsu (porkloin) 13<br>tonkatsu (porkloin) w/ shrimp &amp; vegetable tempura 17</div></div>
    <div class="group"><b>tempura</b> lightly battered &amp; fried with a side of sauce served with miso soup, house salad &amp; rice
      <div class="variants">vegetable 10<br>shrimp &amp; vegetable 17</div></div>
    <div class="group"><b>negimaki</b> sliced meat, scallions &amp; teriyaki sauce served with a side of miso soup, house salad and rice
      <div class="variants">chicken 12<br>beef 15</div></div>
    <div class="group"><b>asparagus maki</b> sliced beef, asparagus &amp; teriyaki sauce served with a side of miso soup, house salad &amp; rice <span class="price">15</span></div>
    <div class="group"><b>bibimbap</b> rice, carrots, beansprouts, daikon, spinach, zucchini, sesame seeds, seaweed flakes, a side of spicy sauce &amp; your choice of raw or fried egg served with miso soup and salad
      <div class="variants">tofu 11<br>chicken 12<br>beef 13</div></div>
    <div class="group"><b>bulgogi</b> thinly sliced beef, carrots &amp; onions served with a side of miso soup, house salad &amp; rice <span class="price">14</span></div>
  </section>
</div>

<div class="column col-right">
  <section class="section" style="top:312px">
    <h2 class="section-title">specials</h2>
    <p class="section-note">lunch specials offered 11am-2:30pm, mon.-sat.</p>
    <p class="item"><b>chicken (9), beef or salmon teriyaki 10</b></p>
    <p class="item"><b>tonkatsu (porkloin) 10</b></p>
    <p class="item"><b>shrimp &amp; vegetable tempura 10</b></p>
    <p class="item"><b>chicken &amp; beef teriyaki 11</b></p>
    <p class="item"><b>beef teriyaki w/ shrimp &amp; vegetable tempura 11</b></p>
    <p class="item"><b>chicken teriyaki w/ shrimp &amp; vegetable tempura 10</b></p>
    <p class="item"><b>salmon teriyaki w/ shrimp &amp; vegetable tempura 11</b></p>
    <p class="item"><b>tonkatsu (porkloin) w/ shrimp &amp; vegetable tempura 11</b></p>
    <p class="item"><b>bento box</b> fried rice, vegetable tempura, fruit, house special, miso soup &amp; house salad
      <span class="variants"><br>beef teriyaki 12<br>chicken teriyaki 11<br>salmon teriyaki 12<br>shrimp tempura 11<br>chicken katsu 11<br>tonkatsu (porkloin) 11</span></p>
    <p class="item"><b>kaiyo box*</b> sashimi (2 pcs of each) salmon, tuna, red snapper, &amp; white tuna; nigiri (1 pc of each) inari, tamago &amp; shrimp; shrimp tempura roll (4 pcs) <span class="price">18</span></p>
    <p class="item"><b>omakase special*</b> nigiri (5 pcs) &amp; 1 california roll <span class="price">12</span></p>
    <p class="item"><b>omakase deluxe*</b> nigiri (6 pcs) &amp; 1 spicy tuna roll <span class="price">13</span></p>
    <p class="item"><b>maki combo*</b> california roll, cucumber roll &amp; tuna roll <span class="price">9</span></p>
    <p class="item"><b>maki combo special*</b> spicy tuna, avocado roll &amp; salmon roll <span class="price">10</span></p>
    <p class="item"><b>chirashi*</b> assorted raw fish &amp; vegetables over rice <span class="price">11</span></p>
  </section>

  <section class="section" style="top:724px">
    <h2 class="section-title">sides</h2>
    <div class="group variants" style="margin-top:-4px">steamed rice 1.5<br>brown rice 1.5<br>sushi rice 2<br>avocado 1.5<br>tofu 1<br>shrimp tempura (1pc.) 2<br>teriyaki sauce 0.5<br>ginger dressing 0.5</div>
  </section>

  <section class="section" style="top:856px">
    <h2 class="section-title">drinks</h2>
    <div class="group variants" style="margin-top:-4px">cola 2<br>diet cola 2<br>lemon-lime soda 2<br>orange soda 2<br>orange or apple juice <span style="font-weight:400">(no refills)</span> 2<br>lemonade 2<br>iced tea 2<br>hot japanese green tea 2</div>
  </section>

  <section class="section" style="top:990px">
    <h2 class="section-title">desserts</h2>
    <p class="item"><b>frushi</b> seasonal fruit wrapped in a maki roll <span class="price">8</span></p>
    <p class="item"><b>mochi ice cream</b> japanese confection<br>w/ ice cream filling <span class="price">4</span></p>
    <p class="item"><b>tempura ice cream</b> fried vanilla ice cream w/ caramel <span class="price">5.5</span></p>
  </section>
</div>

<footer class="footer">
  *These foods contain raw seafood. Consuming raw or partially cooked seafood or shellfish may increase your chances of foodborne illness.<br>
  Prices &amp; availability subject to change. Special request will carry an additional charge.
</footer>

</body>
</html>
```